Stationery Design Project

Require letterhead/stationery design based on new logo (see attached).

Would prefer it kept simple but strong and effective.

Target Market(s)

Clients and building developers. Residential/consumer and corporate clientele.

```html
<!DOCTYPE html>
<html lang="en">
<head>
<meta charset="utf-8">
<title>Northbay Builders – Stationery</title>
<link rel="stylesheet" href="https://fonts.googleapis.com/css2?family=Cormorant+SC:wght@500;600;700&family=Kaushan+Script&display=swap">
<style>
  :root {
    --bg: #5e6062;
    --ink: #141414;
    --paper: #ffffff;
    --accent: #2aa7dc;
    --text: #1c1c1c;
    --muted: #8d8d8d;
    --light: #d9d9d9;
  }
  * { box-sizing: border-box; margin: 0; padding: 0; }
  html, body { width: 1200px; height: 900px; overflow: hidden; }
  body {
    background: var(--bg);
    font-family: "Cormorant SC", Georgia, serif;
    position: relative;
  }

  /* Brand lockup */
  .brand { display: flex; flex-direction: column; align-items: center; gap: 8px; }
  .brand-mark { background: var(--accent); }
  .brand-name { color: var(--light); font-weight: 600; letter-spacing: 0.08em; white-space: nowrap; }

  /* Letterhead */
  .letterhead {
    position: absolute; left: 90px; top: 120px;
    width: 470px; height: 665px;
    background: var(--paper);
    display: flex; flex-direction: column;
  }
  .letterhead-header {
    background: var(--ink); height: 165px;
    display: flex; align-items: center; justify-content: center;
  }
  .letterhead-header .brand-mark { width: 44px; height: 44px; }
  .letterhead-header .brand-name { font-size: 22px; }
  .letter {
    padding: 26px 42px 0; color: var(--text);
    font-size: 9.4px; line-height: 1.45; font-weight: 600;
  }
  .letter-recipient { text-align: center; font-size: 11px; font-weight: 700; margin-bottom: 16px; }
  .letter p { text-align: justify; margin-bottom: 11px; }
  .letter .letter-closing { text-align: center; margin: 14px 0 0; font-size: 10.5px; font-weight: 700; }
  .letter .letter-signature { text-align: center; font-family: "Kaushan Script", cursive; font-size: 13px; margin-top: 2px; }
  .letterhead-footer {
    margin-top: auto; padding-bottom: 34px;
    text-align: center; color: var(--muted); font-size: 10px; line-height: 1.45; font-weight: 600;
  }

  /* Business cards */
  .card {
    position: absolute; left: 680px; width: 350px; height: 200px;
    box-shadow: 0 4px 10px rgba(0,0,0,0.35);
  }
  .card-front {
    top: 175px; background: var(--ink);
    display: flex; align-items: center; justify-content: center;
  }
  .card-front .brand-mark { width: 36px; height: 36px; }
  .card-front .brand-name { font-size: 18px; }
  .card-back { top: 455px; display: flex; background: var(--paper); }
  .card-back-band {
    width: 118px; background: var(--ink);
    display: flex; align-items: center; justify-content: center;
  }
  .card-back-band .brand-mark { width: 24px; height: 24px; }
  .card-back-band .brand-name { font-size: 10px; letter-spacing: 0.04em; }
  .card-back-details { flex: 1; padding: 22px 20px; text-align: right; }
  .card-name { font-size: 15px; font-weight: 700; color: var(--text); line-height: 1.1; }
  .card-role { font-size: 10px; font-weight: 700; color: var(--text); margin-bottom: 12px; }
  .card-contact { font-size: 10px; line-height: 1.5; color: var(--muted); font-weight: 600; }
</style>
</head>
<body>

  <article class="letterhead">
    <header class="letterhead-header">
      <div class="brand">
        <span class="brand-mark"></span>
        <span class="brand-name">Northbay Builders</span>
      </div>
    </header>
    <section class="letter">
      <h2 class="letter-recipient">Mr John Doe</h2>
      <p>Turi ro magnatis et aceribustem hici raecte es eos as eicias ipite sitios asped magnisint. Solor sitiund itius, con rerum sincipsum vellia voluptio omnim quptatio ipsam ium quo offici accae sitation sequist emporem porror assin nemporum venisci unquatecum renimolorum exerit aut et dolorio cor repe magnient qui sequatis doluptas aut amus, sectemp erumqui officipid.</p>
      <p>Orit, te si con et unt qui dis non consed quunt faccae de re nima quis sum harchil luptas nonse cum essum ut porae nonsequo molorem quam harit maiorerit aceptur, utet liquam net que odis arciligniae autaectemque cumetur emperatur rem quatem quis dolluptibus, con rem est et dolorere voluptas acepellenda volupta eiureme luptat laceratur, eum quas aut auda derum idio beri suntio. Apietur, sitectus aborerum voluptatem nostruptatio consendam hic tem auta core.</p>
      <p>El maiorum, volorem volecab in cullab im quaeria toquodia quatem et et re nis in pedicid quasin nime doluptatium faccaeristo blabor aut aut at et rectotae pora non re non commoles dolor sum ipsam fuga. Et vero tem et excepeum quam asserum si dis nonsequam essum et aut adis quis sundeni ium am esenimaiorum quaernam volendamusda quias alita volorepero eostia di con con pari comnis eniet perum ipit is deles aperiae dolorem. Ehentot assimpo restorit pratquas acernatia verio. Nempore pereiusam doluptaquat.</p>
      <p class="letter-closing">Best Regards</p>
      <p class="letter-signature">Mr Alan Reese Director</p>
    </section>
    <footer class="letterhead-footer">
      Northbay Builders<br>
      000-555 0142 | www.northbaybuilders.example | hello@northbaybuilders.example<br>
      12 Harbour Road | Unit 4 | Bayside
    </footer>
  </article>

  <section class="card card-front">
    <div class="brand">
      <span class="brand-mark"></span>
      <span class="brand-name">Northbay Builders</span>
    </div>
  </section>

  <section class="card card-back">
    <div class="card-back-band">
      <div class="brand">
        <span class="brand-mark"></span>
        <span class="brand-name">Northbay Builders</span>
      </div>
    </div>
    <div class="card-back-details">
      <h3 class="card-name">John Doe</h3>
      <p class="card-role">Vice President</p>
      <p class="card-contact">
        000-555 0142<br>
        hello@northbaybuilders.example<br>
        www.northbaybuilders.example<br>
        12 Harbour Road | Bayside
      </p>
    </div>
  </section>

</body>
</html>
```